Business Card, T Shirt ,Fax cover, Letterhead, Invoice
Kovac Painting & Decorating
Professional
Tobias Kovac
Bay no 482, 67 North Amber Way SW
California AB T3K5M8
tobias@kovacpaintworx.com
www.kovacpaintworx.com
Contents of the Invoice

```html
<!DOCTYPE html>
<html lang="en">
<head>
<meta charset="utf-8">
<title>Kovac Painting &amp; Decorating — Business Card</title>
<link rel="stylesheet" href="https://fonts.googleapis.com/css2?family=Lato:wght@700&family=Tinos:wght@700&display=swap">
<style>
  :root {
    --backdrop: #e6d8bb;
    --card-white: #ffffff;
    --brand-green: #2f9a3a;
    --deep-green: #0f6b22;
    --light-green: #7cc24a;
    --accent-orange: #e8781e;
    --shadow: rgba(60, 40, 10, 0.28);
  }
  * { margin: 0; padding: 0; box-sizing: border-box; }
  html, body {
    width: 1200px; height: 878px; overflow: hidden;
    background: var(--backdrop);
  }
  .card {
    position: absolute;
    width: 592px; height: 266px;
    box-shadow: 0 3px 8px var(--shadow);
    overflow: hidden;
  }
  .card--front { left: 305px; top: 72px; background: var(--card-white); }
  .card--back {
    left: 305px; top: 360px;
    background: radial-gradient(ellipse at 50% 45%, var(--light-green) 0%, var(--brand-green) 45%, var(--deep-green) 100%);
  }
  .brand-sweep {
    position: absolute; left: 30px; top: 0; width: 250px; height: 266px;
  }
  .brand-lockup {
    position: absolute; left: 300px; top: 22px;
    display: flex; align-items: center; gap: 12px;
  }
  .brand-lockup__dot {
    width: 44px; height: 44px; border-radius: 50%;
    background: var(--accent-orange);
  }
  .brand-lockup__name {
    font-family: "Tinos", serif; font-weight: 700;
    color: var(--brand-green); line-height: 1;
  }
  .brand-lockup__title { display: block; font-size: 34px; letter-spacing: 2px; }
  .brand-lockup__sub { display: block; font-size: 10.5px; letter-spacing: 0.6px; margin-top: 3px; }
  .contact-list {
    position: absolute; left: 307px; top: 96px;
    list-style: none;
    font-family: "Tinos", serif; font-weight: 700; font-size: 13px;
    color: var(--accent-orange); line-height: 19px;
  }
  .contact-list li { display: flex; }
  .contact-list .label { width: 24px; }
  .contact-list .value { display: block; }
  .holder-name {
    position: absolute; left: 14px; top: 228px;
    font-family: "Lato", sans-serif; font-weight: 700; font-size: 19px;
    color: var(--accent-orange);
  }
  .back-mark {
    position: absolute; left: 228px; top: 76px;
    width: 136px; height: 136px; border-radius: 50%;
    border: 5px solid var(--card-white);
    display: flex; align-items: center; justify-content: center;
    font-family: "Tinos", serif; font-weight: 700; font-size: 28px;
    letter-spacing: 2px; color: var(--card-white);
  }
  .web-address {
    position: absolute; left: 0; right: 0; top: 226px; text-align: center;
    font-family: "Lato", sans-serif; font-weight: 700; font-size: 17px;
    color: var(--card-white);
  }
</style>
</head>
<body>
  <section class="card card--front">
    <svg class="brand-sweep" viewBox="0 0 250 266" role="img" aria-label="Large green brand swirl decoration">
      <defs>
        <linearGradient id="sweepFill" x1="0" y1="0" x2="1" y2="1">
          <stop offset="0" stop-color="#7cc24a" stop-opacity="0.9"/>
          <stop offset="0.55" stop-color="#2f9a3a" stop-opacity="0.85"/>
          <stop offset="1" stop-color="#0f6b22" stop-opacity="0.15"/>
        </linearGradient>
      </defs>
      <rect x="0" y="0" width="250" height="266" fill="url(#sweepFill)"/>
    </svg>

    <div class="brand-lockup">
      <span class="brand-lockup__dot"></span>
      <span class="brand-lockup__name">
        <span class="brand-lockup__title">KOVAC</span>
        <span class="brand-lockup__sub">PAINTING &amp; DECORATING LTD.</span>
      </span>
    </div>

    <ul class="contact-list">
      <li><span class="label">A :</span><span class="value">Bay no 482, 67 North Amber Way SW<br>California,AB T3K5M8</span></li>
      <li><span class="label">P :</span><span class="value">483 610 2040</span></li>
      <li><span class="label">C :</span><span class="value">423 318 4406</span></li>
      <li><span class="label">F :</span><span class="value">423 590 7713</span></li>
      <li><span class="label">E :</span><span class="value">tobias@kovacpaintworx.com</span></li>
    </ul>

    <p class="holder-name">Tobias Kovac</p>
  </section>

  <section class="card card--back">
    <div class="back-mark">KOVAC</div>
    <p class="web-address">www.kovacpaintworx.com</p>
  </section>
</body>
</html>
```